Architectural Design practice needs new logo /letterhead design

We need a new logo / letterhead design to freshen up the practice image. We are an architects practice working in all building design sectors and want a new modern fresh logo / letterhead but retaining a professional feel, so not too gimmicky. The current branding colour palette uses blue and grey, which we still like, but we are also open to other suggestions. I have attached our current letterhead which has served us well and incorporates the FENC logo, but this was produced in-house using only Word when we first started the business and we would now like a new more modern and professional design.
Possibly include the acronym KPT , or kpt, second file added shows an attempt I did myself, which is a bit basic but gives an idea of the type of thing we are looking for

File added showing the type of thing we are looking for

Building

Sans Serif

```html
<!DOCTYPE html>
<html lang="en">
<head>
<meta charset="utf-8">
<title>KPTARN Associates – Letterhead</title>
<link rel="stylesheet" href="https://fonts.googleapis.com/css2?family=Roboto+Condensed:wght@400;700&family=Tinos:wght@400;700&display=swap">
<style>
  :root {
    --paper: #fbfbfb;
    --teal: #3fb3c8;
    --teal-dark: #2c6c78;
    --ink: #3a3a3a;
    --muted: #6b6b6b;
    --rule: #9a9a9a;
    --faint: #ececec;
  }
  * { margin: 0; padding: 0; box-sizing: border-box; }
  html, body { width: 942px; height: 1200px; overflow: hidden; background: var(--paper); }
  .letterhead { position: relative; width: 942px; height: 1200px; background: var(--paper); font-family: "Tinos", "Times New Roman", serif; color: var(--ink); }

  .brand { position: absolute; left: 76px; top: 0; width: 152px; font-family: "Roboto Condensed", Arial, sans-serif; font-weight: 700; color: var(--teal-dark); }
  .brand-square { width: 152px; height: 112px; background: var(--teal); }
  .brand-initials { margin-top: 18px; font-size: 54px; line-height: 1; letter-spacing: 2px; }
  .brand-name { margin-top: 14px; font-size: 17px; line-height: 1.15; letter-spacing: 3px; }
  .brand-tagline { margin-top: 3px; font-size: 7.5px; letter-spacing: 1.6px; }

  .meta { position: absolute; left: 280px; top: 203px; font-size: 11.5px; line-height: 24px; }
  .meta b { font-weight: 700; }

  .letter-body { position: absolute; left: 280px; top: 276px; width: 581px; font-size: 11.5px; line-height: 24.8px; }
  .letter-body p { margin-bottom: 24.8px; text-align: justify; }
  .salutation { margin-bottom: 0 !important; }

  .sign-off { position: absolute; left: 280px; top: 754px; font-size: 11.5px; line-height: 16px; }
  .signature { position: absolute; left: 280px; top: 807px; width: 256px; height: 120px; background: linear-gradient(120deg, var(--paper), #efefef 50%, var(--paper)); }

  .emblem { position: absolute; left: 580px; top: 810px; width: 362px; height: 390px; background: linear-gradient(180deg, var(--faint), #f2f2f2); opacity: .8; }

  .footer { position: absolute; left: 74px; top: 1140px; display: flex; font-family: "Roboto Condensed", Arial, sans-serif; font-size: 9.5px; letter-spacing: 1.3px; line-height: 19px; color: var(--muted); text-transform: uppercase; }
  .footer-col { padding: 0 10px; }
  .footer-col:first-child { padding-left: 0; width: 219px; }
  .footer-col + .footer-col { border-left: 1px solid var(--rule); }
  .footer-col b { color: var(--ink); }
</style>
</head>
<body>
<main class="letterhead">
  <header class="brand">
    <div class="brand-square"></div>
    <div class="brand-initials">KPT</div>
    <div class="brand-name">KPTARN<br>ASSOCIATES</div>
    <div class="brand-tagline">CHARTERED ARCHITECTS</div>
  </header>

  <section class="meta">
    <div><b>Data :</b> Mon , 25 / 3 / 2013</div>
    <div><b>Recipient :</b> Mr.John Doe Hartwell</div>
  </section>

  <article class="letter-body">
    <p class="salutation">Dear Mr. Jhon Doe</p>
    <p>LoTrem ipsum dolor sit amet, consectetur adipiscing elit. Praesent vulputate, neque ac accumsan suscipit, justo turpis volutpat nisl, tempus fermentum eros tortor et elit. Vivamus porttitor faucibus gravida. Quisque pharetra gravida luctus. Donec eget turpis libero. Ut ac dolor urna, quis tempor nunc. Donec vitae mauris purus, euismod eleifend nulla. Lorem ipsum dolor sit amet, consectetur adipiscing elit. Donec ut purus tellus. Aenean quis dignissim lacus. Vestibulum suscipit vehicula cursus. Suspendisse potenti. Ut in sem nisi. Sed et massa leo.</p>
    <p>Fusce varius libero vel risus condimentum suscipit. Nullam tristique ultrices massa a volutpat. Donec sed dictum metus. Curabitur fringilla nibh eu ligula pharetra a interdum quam aliquam. Maecenas aliquam elit eu orci rutrum molestie. Proin nisl justo, varius a volutpat nec, ultricies sed sem. Nam sit amet imperdiet sem. Phasellus vitae mauris odio. Etiam in purus dui. Etiam ultricies, ante vel iaculis sodales, arcu leo adipiscing leo, sit amet mollis dui nisi non quam.</p>
    <p>Suspendisse sagittis laoreet dolor, vitae rhoncus arcu volutpat quis. Vestibulum at placerat dolor. Vivamus eu lacus ut enim molestie consectetur. Quisque ac lorem vel orci sagittis sollicitudin. Nunc ut quam sem, quis volutpat libero. Cum sociis natoque penatibus et magnis dis parturient montes, nascetur ridiculus mus. Vestibulum ante ipsum primis in faucibus orci luctus et ultrices posuere cubilia Curae; Donec tempor velit in velit feugiat sit amet vulputate nisl posuere..</p>
  </article>

  <section class="sign-off">
    <div>JOHN DOE</div>
    <div>General director</div>
  </section>
  <div class="signature" role="img" aria-label="Handwritten signature of the general director"></div>

  <div class="emblem" role="img" aria-label="Faint decorative emblem of a heraldic lion beside a tower"></div>

  <footer class="footer">
    <div class="footer-col">Larch Court, 14 Millbrook Lane<br>Redhill, Surrey, RH9 4QT</div>
    <div class="footer-col"><b>P.</b> 01632 960418<br><b>F.</b> 01632 960427</div>
    <div class="footer-col"><b>E.</b> enquiry@kptarnassociates.co.uk<br><b>W.</b> www.kptarnassociates.co.uk</div>
  </footer>
</main>
</body>
</html>
```